Tarjetas de visita para empresa de aluminio

Empresa con mas de 40 años vendiendo perfiles de aluminio.
Somos fábrica y almacén, queremos renovar la tarjeta de presentación de nuestros comerciales dando una imgen innovadora y tecnógica mezclado con la calidez del respeto al medio ambiente.
Añado el logo de la empresa y actual cara trasera de la tarjeta de visita, el logo es el simbolo WM y la marca TRAVENIC EXTRUSION, la frase 2extrusion y lacado de aluminio" debe cambiarse por "Diseño, extrusión, lacado, anodizado y mecanizado de precisión de aluminio" o en su defecto incluir todos esos servicios que hacemos o una frase mas pegadiza.

We are an aluminium factory, we produce and stock profiles of aluminium.
we want to renew visit card of our sellers, we are looking for something that show innovation, tecnology and environment respect.
Upload our actual logo and back of visit card, logo WM and brand TRAVENIC EXTRUSION must be keept.
Text "Extrusion y lacado de aluminio" must be changed for "Diseño, extrusion, lacado, anodizado y mecanizado de precisión de aluminio" or something like that

```html
<!DOCTYPE html>
<html lang="es">
<head>
<meta charset="utf-8">
<title>Tarjeta de visita – Travenic Extrusion</title>
<link href="https://fonts.googleapis.com/css2?family=Lato:wght@400;700&family=Libre+Baskerville&display=swap" rel="stylesheet">
<style>
  :root {
    --bg: #9a9c9b;
    --card-front: #fbfbfb;
    --navy: #2a5282;
    --steel: #7a7b7e;
    --ink: #4d4d4d;
    --card-back: #2a2a2a;
    --card-back-light: #333334;
    --silver: #e4e4e4;
    --silver-dim: #c4c4c4;
  }
  html, body {
    margin: 0;
    width: 1200px;
    height: 1200px;
    overflow: hidden;
    background: var(--bg);
  }
  .card {
    position: absolute;
    left: 222px;
    width: 755px;
    height: 463px;
    font-family: "Lato", sans-serif;
  }
  .card--front { top: 105px; background: var(--card-front); }
  .card--back {
    top: 630px;
    background: radial-gradient(ellipse at 50% 45%, var(--card-back-light), var(--card-back) 70%);
  }

  .holder-name {
    position: absolute; left: 48px; top: 72px; margin: 0;
    font-family: "Libre Baskerville", serif; font-weight: 400;
    font-size: 29px; color: var(--navy); letter-spacing: -0.5px;
  }
  .holder-role {
    position: absolute; left: 48px; top: 112px; margin: 0;
    font-family: "Libre Baskerville", serif; font-size: 28px; color: var(--ink);
  }
  .address {
    position: absolute; left: 48px; top: 164px; margin: 0;
    font-style: normal; font-size: 18px; line-height: 23.5px; color: var(--ink);
  }
  .contacts {
    position: absolute; left: 48px; top: 278px; margin: 0; padding: 0;
    list-style: none; font-size: 21px; color: var(--ink);
  }
  .contacts li { display: flex; align-items: center; height: 29px; }
  .contacts li:nth-child(4) { margin-top: 2px; }
  .contacts li:nth-child(5) { margin-top: 4px; }
  .contacts svg { width: 22px; height: 22px; margin-right: 10px; fill: var(--navy); flex: none; }
  .contacts .icon-globe { fill: none; stroke: var(--navy); stroke-width: 1.6; }

  .brand-front {
    position: absolute; left: 375px; top: 262px; width: 355px; text-align: center;
  }
  .brand-front .brand-dot {
    display: block; margin: 0 auto 16px; width: 64px; height: 64px;
    border-radius: 50%; border: 3px solid var(--steel);
  }
  .brand-front .brand-name {
    margin: 0; font-weight: 700; font-size: 22px; letter-spacing: 1.5px; color: #3a3a3a;
  }
  .brand-front .brand-tag {
    margin: 6px 0 0; font-weight: 700; font-size: 11px; line-height: 15px;
    letter-spacing: 0.9px; color: var(--navy); text-transform: uppercase;
  }

  .edge-band { position: absolute; bottom: 0; height: 18px; }
  .edge-band--left { left: 0; width: 398px; background: var(--navy); }
  .edge-band--mid { left: 404px; width: 296px; background: var(--steel); }
  .edge-band--right { left: 706px; width: 49px; background: var(--navy); }

  .brand-back { position: absolute; left: 0; top: 125px; width: 100%; text-align: center; }
  .brand-back .brand-dot {
    display: block; margin: 0 auto 36px; width: 110px; height: 110px;
    border-radius: 50%; border: 4px solid var(--silver-dim);
  }
  .brand-back .brand-name {
    margin: 0; font-weight: 400; font-size: 36px; letter-spacing: 3px; color: var(--silver);
  }
  .brand-back .brand-tag {
    margin: 14px 0 0; font-weight: 400; font-size: 16px; line-height: 24px;
    letter-spacing: 2.5px; color: var(--silver-dim); text-transform: uppercase;
  }
</style>
</head>
<body>
  <section class="card card--front">
    <h1 class="holder-name">MARCOS LEDESMA RUIZ</h1>
    <p class="holder-role">Comercial</p>
    <address class="address">
      Pol. Ind. Norvalle - C/4 Nº 22<br>
      41530 SAN MARTÍN DEL ARCO (Sevilla)<br>
      Apartado de Correos 245
    </address>
    <ul class="contacts">
      <li><svg viewBox="0 0 24 24" aria-hidden="true"><path d="M7 1h10a2 2 0 0 1 2 2v18a2 2 0 0 1-2 2H7a2 2 0 0 1-2-2V3a2 2 0 0 1 2-2zm0 3v14h10V4zm5 15.5a1.2 1.2 0 1 0 0 2.4 1.2 1.2 0 0 0 0-2.4z"/></svg>600 12 34 56</li>
      <li><svg viewBox="0 0 24 24" aria-hidden="true"><path d="M2 8c0-3 5-4 10-4s10 1 10 4v2h-5V8H7v2H2zm4 3h12l3 10H3zm6 2a3 3 0 1 0 0 6 3 3 0 0 0 0-6z"/></svg>955 00 12 47</li>
      <li><svg viewBox="0 0 24 24" aria-hidden="true"><path d="M6 2h12v6H6zM3 9h18a2 2 0 0 1 2 2v7h-5v4H6v-4H1v-7a2 2 0 0 1 2-2zm5 6v5h8v-5z"/></svg>955 00 12 47</li>
      <li><svg viewBox="0 0 24 24" aria-hidden="true"><path d="M1 4h20v9h-2V7l-8 6-8-6v11h11v2H1zm2 0 8 6 8-6zm15 11 2 2 3-4 1 1-4 5-3-3z"/></svg>marcosledesma@travenic.com</li>
      <li><svg class="icon-globe" viewBox="0 0 24 24" aria-hidden="true"><circle cx="12" cy="12" r="10"/><ellipse cx="12" cy="12" rx="4.5" ry="10"/><path d="M2 12h20M3.5 7h17M3.5 17h17M12 2v20"/></svg>www.travenic.com</li>
    </ul>
    <div class="brand-front">
      <span class="brand-dot"></span>
      <p class="brand-name">TRAVENIC EXTRUSION</p>
      <p class="brand-tag">Diseño, extrusión, lacado, anodizado<br>y mecanizado de precisión de aluminio</p>
    </div>
    <div class="edge-band edge-band--left"></div>
    <div class="edge-band edge-band--mid"></div>
    <div class="edge-band edge-band--right"></div>
  </section>

  <section class="card card--back">
    <div class="brand-back">
      <span class="brand-dot"></span>
      <p class="brand-name">TRAVENIC EXTRUSION</p>
      <p class="brand-tag">Diseño, extrusión, lacado, anodizado<br>y mecanizado de precisión de aluminio</p>
    </div>
  </section>
</body>
</html>
```